TWS Business Card Design

As a full service media and advocacy firm, we lean on years of experience in political and corporate consulting, grassroots campaigning, media placement, and video production to deliver unparalleled results. Recently we have moved into digital media and now provide this service for our clients.

I will add our two company logos to be used on the business cards. The longer logo with "sky reach studio" is our primary logo. Our secondary logo is more square one with "sky reach" and 'digital.media.campaigns" on it. We are looking for clean and modern looking business cards fitting for a digital firm.

I will also add our logos that go well with dark backgrounds.

Industry/Entity Type

Political

Contact Information for Business Card

Denton Pratchard, Director of Campaigns and Digital, 571-482-7165, denton@skyreachstudioco.com, @SkyReachStudioCo, @DentonPratchard, Facebook.com/SkyReachStudioCo

```html
<!DOCTYPE html>
<html lang="en">
<head>
<meta charset="utf-8">
<title>Sky Reach Studio – Business Card</title>
<link href="https://fonts.googleapis.com/css2?family=Open+Sans:ital,wght@0,400;0,600;0,700;1,400&display=swap" rel="stylesheet">
<style>
  :root {
    --backdrop: #2c3767;
    --navy: #1b2a6b;
    --navy-deep: #16215a;
    --brand-blue: #1f7fd0;
    --paper: #f3f5fb;
    --ink-light: #ffffff;
  }
  * { margin: 0; padding: 0; box-sizing: border-box; }
  html, body {
    width: 1200px; height: 952px; overflow: hidden;
    background: var(--backdrop);
    font-family: "Open Sans", Arial, sans-serif;
  }
  .stage { position: relative; width: 1200px; height: 952px; }
  .card {
    position: absolute; top: 333px;
    width: 500px; height: 286px;
    border-radius: 6px; overflow: hidden;
    box-shadow: 0 12px 30px rgba(0,0,0,0.35);
  }
  .card-front {
    left: 70px;
    background: linear-gradient(135deg, #22307a 0%, var(--navy-deep) 100%);
    display: flex; align-items: center; justify-content: center;
  }
  .primary-name {
    font-weight: 700; font-size: 44px; letter-spacing: 1px;
    color: var(--brand-blue); text-transform: uppercase;
  }
  .card-back { left: 630px; background: var(--paper); }
  .accent-area {
    position: absolute; left: 200px; top: 110px; right: 0; bottom: 0;
    background: linear-gradient(90deg, rgba(27,42,107,0) 0%, var(--navy) 14%, var(--navy-deep) 100%);
  }
  .secondary-logo {
    position: absolute; left: 26px; top: 34px;
    display: flex; align-items: center; gap: 10px;
  }
  .secondary-name {
    font-weight: 700; font-size: 40px; text-transform: uppercase;
    color: var(--navy); letter-spacing: 0.5px;
  }
  .logo-dot { width: 14px; height: 14px; border-radius: 50%; background: var(--brand-blue); }
  .person { position: absolute; left: 26px; top: 160px; }
  .person-name { font-weight: 700; font-size: 19px; color: var(--navy); }
  .person-title { font-style: italic; font-size: 12px; color: var(--brand-blue); margin-top: 2px; }
  .contacts {
    position: absolute; right: 18px; top: 130px;
    list-style: none; text-align: right;
  }
  .contacts li {
    display: flex; justify-content: flex-end; align-items: center; gap: 8px;
    color: var(--ink-light); font-size: 13px; line-height: 26px;
  }
  .contacts svg { width: 13px; height: 13px; flex: none; }
</style>
</head>
<body>
<main class="stage">

  <section class="card card-front" aria-label="Card front">
    <span class="primary-name">Sky Reach Studio</span>
  </section>

  <section class="card card-back" aria-label="Card back">
    <div class="accent-area" role="img" aria-label="Decorative navy and blue wave band"></div>

    <div class="secondary-logo">
      <span class="secondary-name">Sky Reach</span>
      <span class="logo-dot"></span>
    </div>

    <div class="person">
      <p class="person-name">Denton Pratchard</p>
      <p class="person-title">Director of Campaigns &amp; Digital</p>
    </div>

    <ul class="contacts">
      <li>571-482-7165
        <svg viewBox="0 0 16 16" aria-hidden="true"><path d="M3 1h3l1.5 4-2 1.5a9 9 0 0 0 4 4L11 8.5l4 1.5v3a2 2 0 0 1-2 2A13 13 0 0 1 1 3a2 2 0 0 1 2-2z" fill="#fff"/></svg>
      </li>
      <li>/SkyReachStudioCo
        <svg viewBox="0 0 16 16" aria-hidden="true"><rect x="1" y="1" width="14" height="14" rx="2" fill="#fff"/></svg>
      </li>
      <li>@SkyReachStudioCo
        <svg viewBox="0 0 16 16" aria-hidden="true"><rect x="1" y="3" width="14" height="10" fill="#fff"/><path d="M1 3l7 6 7-6" fill="none" stroke="var(--navy)" stroke-width="1.3"/></svg>
      </li>
      <li>@DentonPratchard
        <svg viewBox="0 0 16 16" aria-hidden="true"><rect x="1" y="3" width="14" height="10" fill="#fff"/><path d="M1 3l7 6 7-6" fill="none" stroke="var(--navy)" stroke-width="1.3"/></svg>
      </li>
      <li>denton@skyreachstudioco.com
        <svg viewBox="0 0 16 16" aria-hidden="true"><rect x="1" y="3" width="14" height="10" fill="#fff"/><path d="M1 3l7 6 7-6" fill="none" stroke="var(--navy)" stroke-width="1.3"/></svg>
      </li>
    </ul>
  </section>

</main>
</body>
</html>
```